KORBALT

The business want a professional looking business card. We have a scetch we will add but want the extra upgrade, and would like more suggestions for variations of our business cards.

```html
<!DOCTYPE html>
<html lang="en">
<head>
<meta charset="utf-8">
<title>KORBALT – Business Card</title>
<link rel="stylesheet" href="https://fonts.googleapis.com/css2?family=Marcellus&family=Oswald:wght@400&family=Montserrat:wght@600&display=swap">
<style>
  :root {
    --page-bg: #ffffff;
    --gold-light: #ede5d5;
    --gold-mid: #bb9c5e;
    --gold-dark: #6f5021;
    --ink: #6a481a;
    --ink-soft: #d8bf8a;
  }
  * { box-sizing: border-box; margin: 0; padding: 0; }
  html, body { width: 1200px; height: 1200px; overflow: hidden; background: var(--page-bg); }
  .canvas {
    width: 1200px; height: 1200px;
    display: flex; align-items: center; justify-content: center; gap: 40px;
  }
  .card {
    position: relative;
    width: 560px; height: 340px;
    background: linear-gradient(90deg, var(--gold-light) 0%, var(--gold-mid) 50%, var(--gold-dark) 100%);
    color: var(--ink);
    overflow: hidden;
  }
  /* Front */
  .card-front { display: flex; align-items: center; justify-content: center; }
  .front-name {
    font-family: "Marcellus", serif;
    font-size: 62px;
    letter-spacing: 0.28em;
    padding-left: 0.28em;
    color: var(--ink);
    margin-top: -20px;
  }
  /* Back */
  .back-title {
    position: absolute; top: 22px; left: 0; right: 0;
    text-align: center;
    font-family: "Marcellus", serif;
    font-size: 30px; letter-spacing: 0.04em;
  }
  .back-divider {
    position: absolute; left: 280px; top: 78px; bottom: 12px;
    width: 2px; background: var(--ink);
  }
  .holder { position: absolute; left: 14px; top: 112px; }
  .holder-name {
    font-family: "Oswald", sans-serif;
    font-size: 19px; text-decoration: underline; text-underline-offset: 2px;
    line-height: 1.1;
  }
  .holder-role {
    font-family: "Montserrat", sans-serif; font-weight: 600;
    font-size: 12px; letter-spacing: 0.03em;
  }
  .contacts { position: absolute; left: 14px; top: 196px; list-style: none; }
  .contact {
    display: flex; align-items: center; gap: 9px;
    font-family: "Oswald", sans-serif; font-size: 17px;
    height: 33px;
  }
  .contact svg { width: 22px; height: 22px; flex: none; }
  .back-brand {
    position: absolute; left: 282px; right: 0; top: 230px;
    display: flex; align-items: center; justify-content: center; gap: 10px;
    font-family: "Marcellus", serif; font-size: 26px; letter-spacing: 0.2em;
    color: var(--ink-soft);
  }
  .brand-dot { width: 12px; height: 12px; border-radius: 50%; background: var(--ink-soft); }
</style>
</head>
<body>
<main class="canvas">
  <section class="card card-front" aria-label="Business card front">
    <div class="front-name">KORBALT</div>
  </section>

  <section class="card card-back" aria-label="Business card back">
    <h1 class="back-title">KORBALT HOLMVIK</h1>
    <div class="back-divider"></div>
    <div class="holder">
      <div class="holder-name">ANDERS LUNDE HOLMVIK</div>
      <div class="holder-role">CEO &amp; FOUNDER</div>
    </div>
    <ul class="contacts">
      <li class="contact">
        <svg viewBox="0 0 24 24" fill="none" stroke="currentColor" stroke-width="1.5"><circle cx="12" cy="12" r="10.5"/><path d="M12 18s-4-4.3-4-7.2a4 4 0 0 1 8 0C16 13.7 12 18 12 18z"/><circle cx="12" cy="10.8" r="1.4"/></svg>
        Address
      </li>
      <li class="contact">
        <svg viewBox="0 0 24 24" fill="none" stroke="currentColor" stroke-width="1.5"><circle cx="12" cy="12" r="10.5"/><path d="M8.5 7.5l2 2-1 1.5a7 7 0 0 0 3.5 3.5l1.5-1 2 2-1.5 1.5c-3.5 0-8-4.5-8-8z"/></svg>
        Phone number
      </li>
      <li class="contact">
        <svg viewBox="0 0 24 24" fill="none" stroke="currentColor" stroke-width="1.5"><circle cx="12" cy="12" r="10.5"/><rect x="7" y="8.5" width="10" height="7"/><path d="M7 8.5l5 4 5-4"/></svg>
        e-mail
      </li>
      <li class="contact">
        <svg viewBox="0 0 24 24" fill="none" stroke="currentColor" stroke-width="1.5"><circle cx="12" cy="12" r="10.5"/><circle cx="12" cy="12" r="5.5"/><path d="M6.5 12h11M12 6.5c-2 2.8-2 8.2 0 11M12 6.5c2 2.8 2 8.2 0 11"/></svg>
        Website
      </li>
    </ul>
    <div class="back-brand"><span class="brand-dot"></span>KORBALT</div>
  </section>
</main>
</body>
</html>
```